Product Description page for Hullwrap.com, References here just need a clean up redesign

Hi, were working on updating the product description page of our site hullwrap.com

Attached is a reference of what we drew on paint. We want to keep it pretty much the same as far as whats on there, the components with a few small adjustments and a clean actually designed look.

1. We want to remove the tabs (product description, warranty, reviews) and put it all in that main content area stretching down into sections. IE: Product Description section, followed by reviews, followed by warranty, below each other.
2. The side bar needs to be redesigned as far as the look and feel but the content and whats in there should stay the same.
3. The main banner area will be replaced shortly you do not have to worry about that.
4. Include a section or box for people to put in their email for a free Ebook.

Target Market(s)

people looking to easily view our boat cover products and buy without having to click too often or leave the page.

Industry/Entity Type

Online Shopping

Number of Pages Required

1 page

Requirements
Must have
• - Must update the sidebar
• - Must update the content area to remove the tabs and put the content from each tab sectioned off below each other (dummy text is fine for now for the tabs you cant view)
Nice to have
• - Cool place thats clean and functional to insert a section for people to put in their email to receive a free ebook
Should not have
• - too much change, we already know what we want and have a solid reference to work from.

```html
<!DOCTYPE html>
<html lang="en">
<head>
<meta charset="utf-8">
<title>Hullwrap.com – Pro Bass Boat Cover</title>
<link href="https://fonts.googleapis.com/css2?family=Open+Sans:wght@400;600;700&family=Roboto+Condensed:wght@700&display=swap" rel="stylesheet">
<style>
:root{
  --blue:#1a3f9e;
  --blue-dark:#0d2a7a;
  --blue-link:#1f4fb0;
  --green:#3a9a1e;
  --red:#e0261b;
  --text:#444;
  --muted:#777;
  --rule:#d6d6d6;
  --side:#efefef;
  --nav:#e6e6e6;
}
*{box-sizing:border-box;margin:0;padding:0}
html,body{width:1200px;height:1200px;overflow:hidden;background:#fff}
body{font-family:"Open Sans",Arial,sans-serif;color:var(--text)}
.stage{position:absolute;left:0;top:0;width:1500px;height:1500px;transform:scale(.8);transform-origin:0 0}
.page{position:absolute;left:497px;top:0;width:506px;height:1500px;background:#fff}
.abs{position:absolute}
/* header */
.brand{left:68px;top:8px;font-weight:700;font-size:10px;color:#1b2b55;letter-spacing:-.2px;display:flex;align-items:center;gap:4px}
.brand .dot{width:9px;height:9px;background:var(--blue);border-radius:50%}
.brand small{position:absolute;left:13px;top:12px;font-size:4.5px;letter-spacing:1.6px;font-weight:600;color:#555}
.phone{right:66px;top:5px;font-family:"Roboto Condensed",sans-serif;font-size:11px;color:var(--blue);display:flex;gap:4px;align-items:center}
.hours{right:66px;top:18px;font-size:4.5px;color:var(--muted)}
.nav{left:0;top:30px;width:506px;height:16px;background:linear-gradient(#f4f4f4,#dcdcdc);border-top:1px solid #cfcfcf}
.nav ul{list-style:none;display:flex;position:absolute;left:66px;top:4px;gap:0;font-size:6px;color:#555}
.nav li{margin-right:18px}
.checkout{left:365px;top:31px;width:75px;height:12px;background:var(--blue-link);color:#fff;font-size:4.5px;font-weight:700;display:flex;align-items:center;gap:3px;padding-left:6px}
.banner{left:0;top:46px;width:506px;height:30px;background:linear-gradient(#2a58c8,var(--blue-dark))}
.banner h1{position:absolute;left:65px;top:9px;font-family:"Roboto Condensed",sans-serif;font-size:10.5px;color:#fff;font-weight:700}
.crumbs{left:67px;top:86px;font-size:4.5px;color:#666}
.crumbs b{color:var(--blue-link);font-weight:600}
/* gallery */
.thumb{width:34px;height:34px}
.hero-shot{left:170px;top:120px;width:250px;height:115px;background:radial-gradient(ellipse at 50% 45%,#c9ccd2 0 40%,#e9eaec 60%,#fff 75%)}
/* main */
.main{left:65px;width:238px;font-size:5.2px;line-height:10.5px}
.prod-title{font-size:8.6px;line-height:10.5px;color:#333}
.h2{font-size:7px;font-weight:700;color:var(--blue);line-height:10px}
.h3{font-size:5.2px;font-weight:700;color:var(--green)}
.features{list-style:none}
.features li::before{content:"• ";color:#333}
.reviewer{font-weight:700;color:var(--green)}
.stars{color:#f0a020;letter-spacing:-.5px}
label{display:block;font-size:5px;line-height:8px}
.field{height:11px;border:1px solid #bbb;margin-bottom:5px;width:235px}
.area{height:60px}
.btn{display:inline-flex;align-items:center;justify-content:center;background:var(--blue-dark);color:#fff;font-size:6px;border-radius:2px}
/* sidebar */
.side{left:310px;top:240px;width:131px;height:638px;background:var(--side)}
.side .in{position:absolute;left:12px;width:108px;font-size:5px}
.price{font-size:12px;color:var(--red);top:10px}
.kv{display:grid;grid-template-columns:54px 1fr;line-height:8px}
.kv b{font-weight:700;color:#333}
.select{width:36px;height:8px;border:1px solid #bbb;background:#fff;font-size:4.3px;padding-left:3px;line-height:6px;position:relative}
.select::after{content:"";position:absolute;right:3px;top:2px;border:2px solid transparent;border-top-color:#333}
.free{color:var(--green);font-weight:600;font-size:6px}
.side-h{color:var(--blue-link);font-weight:600;font-size:6px}
.fbt{display:flex;gap:4px;height:37px;border-top:1px solid var(--rule);padding-top:4px;width:108px}
.fbt .pic{width:29px;height:25px;background:linear-gradient(#d8dbe1,#9ea5b2)}
.fbt p{line-height:6.5px;font-size:4.6px}
.fbt strong{font-weight:400;font-size:6px;color:#333}
.fbt em{font-style:normal;color:var(--red);font-weight:700;font-size:6px}
.box{width:105px;border:1px solid #ccc;background:#fff}
.lorem{font-size:4.8px;line-height:7.8px;color:#555}
.ebook-h{font-size:11.5px;color:var(--blue)}
.ebook-h span{color:var(--red)}
.email{width:105px;height:11px;border:1px solid #bbb;background:#fff;font-size:4.3px;padding-left:3px;line-height:9px;color:#666}
/* footer */
.scene{left:0;top:1375px;width:506px;height:70px;background:linear-gradient(#fff 0%,#c8d3e2 25%,#8ea2bd 55%,#3d5f8e 80%,#234d8c 100%)}
.foot{left:0;top:1440px;width:506px;height:60px;background:linear-gradient(#1e4aa6,var(--blue-dark))}
.signup{left:66px;top:10px;width:374px;height:12px;background:#0b2470;display:flex;align-items:center;font-size:4.6px;color:#fff;font-weight:700}
.signup .inp{width:72px;height:8px;background:#fff;margin-left:8px}
.signup .sub{background:#f06a12;height:8px;padding:0 5px;display:flex;align-items:center}
.signup .links{margin-left:auto;margin-right:8px;text-decoration:underline;display:flex;gap:5px}
.copy{left:0;width:506px;top:38px;text-align:center;font-size:4px;line-height:5.5px;color:#9fb0d8}
</style>
</head>
<body>
<div class="stage">
<div class="page">

  <!-- header -->
  <div class="abs brand"><span class="dot"></span>HULLWRAP.COM<small>SINCE 1999</small></div>
  <div class="abs phone">
    <svg width="10" height="8" viewBox="0 0 10 8"><path d="M1 3c0-2 8-2 8 0v1H7V3H3v1H1z M2 4h6l1 4H1z" fill="#1f4fb0"/></svg>(800) 555-0184</div>
  <div class="abs hours">Store Hours(M-F, 9:30AM - 6PM PST)</div>
  <nav class="abs nav"><ul><li>Boat Covers</li><li>Bass Boat Covers</li><li>T Top Boat Covers</li><li>Bimini Tops</li><li>Jet Ski Covers</li></ul></nav>
  <div class="abs checkout">
    <svg width="7" height="6" viewBox="0 0 7 6"><path d="M0 0h1.5l1 4h3.5l1-3H2" fill="none" stroke="#fff" stroke-width=".8"/><circle cx="3" cy="5.3" r=".6" fill="#fff"/><circle cx="5.6" cy="5.3" r=".6" fill="#fff"/></svg>CHECKOUT : (0) Items ▾</div>
  <header class="abs banner"><h1>up to 15'8" Long and 77" Wide</h1></header>
  <div class="abs crumbs">Home &gt; &nbsp;Boat Covers &gt; &nbsp;Pro Bass Boat &gt; &nbsp;<b>up to 15'8" Long and 77" Wide</b></div>

  <!-- gallery -->
  <div class="abs thumb" style="left:66px;top:115px;background:linear-gradient(#eee,#b9a48a)" role="img" aria-label="Five star fit badge thumbnail"></div>
  <div class="abs thumb" style="left:104px;top:115px;background:linear-gradient(#3a6ab0,#173a7a)" role="img" aria-label="Cover fabric in blue thumbnail"></div>
  <div class="abs thumb" style="left:66px;top:153px;background:linear-gradient(#b0b0b0,#6d6d6d)" role="img" aria-label="Strap detail thumbnail"></div>
  <div class="abs thumb" style="left:104px;top:153px;background:linear-gradient(#8a8a8a,#4e4e4e)" role="img" aria-label="Fabric texture thumbnail"></div>
  <div class="abs thumb" style="left:66px;top:191px;background:linear-gradient(#444,#111)" role="img" aria-label="Storage bag thumbnail"></div>
  <div class="abs thumb" style="left:104px;top:191px;background:linear-gradient(#ccc,#8d8d8d)" role="img" aria-label="Hem cord detail thumbnail"></div>
  <div class="abs hero-shot" role="img" aria-label="Gray cover strapped over a boat on a trailer"></div>

  <!-- main content -->
  <div class="abs main prod-title" style="top:243px">Fits: Pro Bass Boat up to 15'8"<br>Long and 77" Wide</div>

  <section class="abs main" style="top:270px">
    <h2 class="h2">Description:</h2>
    <p style="margin-top:4px">When a boat is stored outside it is exposed to harmful elements such as wind, dirt, rain, and UV. The Titan Guard is the most powerful cover available providing 10x more strength and protection compared to the competition. The 1200 denier fabric is 100% waterproof and provides excellent protection against sun, rain, wind and snow.</p>
  </section>

  <section class="abs main" style="top:333px">
    <h2 class="h2">Features:</h2>
    <ul class="features" style="margin-top:4px">
      <li>5 Star Fit, Fit guaranteed or your money back</li>
      <li>10 Year Warranty. Full warranty covering rips and tears</li>
      <li>The covers comes in Grey, Blue and Maroon</li>
      <li>The fabric is pure 100% Marine Polyester (no cotton mix)</li>
      <li>No worries, the cover won't stretch or shrink</li>
      <li>Rain or sleet the cover is 100% waterproof</li>
      <li>Fully Breathable, you'll never see mold or mildew</li>
      <li>UV resistant and also prevents heat buildup</li>
      <li>Fully Trailerable (straps included)</li>
      <li>The cover also comes with an integrated hem cord to be used when mooring or on boat lifts</li>
      <li>Tough - Strong - Durable</li>
    </ul>
  </section>

  <section class="abs main" style="top:469px">
    <h2 class="h2">Reviews:</h2>
    <div style="margin-top:11px"><span class="reviewer">Marcus T.</span> &nbsp;<span class="stars">★★★★★</span></div>
    <p>Star RatingStar RatingStar RatingStar Rating</p>
    <p>"This item is quite heavy duty and rides well. It is also great quality. We are pleased with the cover and I would recommend it to anyone who wants a great fit and strong cover."</p>
    <div style="margin-top:11px"><span class="reviewer">Dale</span> &nbsp;<span class="stars">★★★★★</span></div>
    <p>Star RatingStar RatingStar RatingStar Rating</p>
    <p>"I have this on my runabout and it fits great. I feel better with my boat covered and this is a very nice cover. The price was nice especially if you have seen the price on factory covers. I would definitely buy this again and recommend to anyone with boat."</p>
    <div style="margin-top:11px"><span class="reviewer">Ramon</span> &nbsp;<span class="stars">★★★★★</span></div>
    <p>Star RatingStar RatingStar RatingStar Rating</p>
    <p>"I bought 2 of these for 2 boats I own. They have been fabulous so far. We will see how they survive the winter."</p>
  </section>

  <form class="abs main" style="top:659px">
    <label>*Nickname</label><div class="field"></div>
    <label>*Summary of Your Review</label><div class="field"></div>
    <label>*Review</label><div class="field area"></div>
    <div class="btn" style="width:64px;height:16px;margin-top:3px">Submit Review</div>
  </form>

  <section class="abs main" style="top:815px">
    <h2 class="h2">Warranty</h2>
    <h3 class="h3" style="margin-top:10px">Returns &amp; Refunds</h3>
    <p>If you are not 100% satisfied with your purchase, you can return or exchange your order. (Returns must be unworn, in the state you received them, and in the original packaging).</p>
    <p style="margin-top:10.5px">Harbor Deal Covers will process all returns and refunds within 30 days of original order date. After 30 days all orders are final. For the full details on our returns or exchange policy please read below.</p>
    <p style="margin-top:10.5px">Harbor Deal Covers guarantees the covers you purchase will arrive in new condition, be free of defects and will properly fit the vehicle for which you ordered. If your item fails to meet the criteria above Harbor Deal Covers will exchange or return the item.</p>
    <h3 class="h3" style="margin-top:10.5px">Returning Titan Guard Covers</h3>
    <p>Titan Guard covers are 5 Star Fit Covers. The fit and quality are 100% guaranteed or your money back. You have 30 days to try the cover. If you are not 100% satisfied feel free to return or exchange it hassle free. No restocking fee's, we even pay for the shipping.</p>
    <h3 class="h3" style="margin-top:10.5px">Returning SeaShield Covers</h3>
    <p>SeaShield covers are 4 Star Fit Covers. SeaShield covers are semi custom covers based on boat style, length and width. The cover is fully exchangeable.. A small 15% restocking fee is applied when returning or exchanging this cover. You have 30 days to return or exchange the cover. If you are not 100% satisfied, give us a call and will help return or exchange it. We even pay for the shipping.</p>
    <h3 class="h3" style="margin-top:10.5px">Returning SunMate Covers</h3>
    <p>SeaShield covers are 3 Star Fit Covers. SunMate covers are universal covers based on length and width. A small 15% restocking fee is applied when returning or exchanging this cover. You have 30 days to return or exchange the cover. If you are not 100% satisfied, give us a call and will help return or exchange it. We even pay for the shipping.</p>
  </section>

  <section class="abs main" style="top:1161px">
    <h2 class="h2">Shipping</h2>
    <p style="margin-top:11px">Unlike many other web sites that have special rules and lots of fine print, Harbor Deal Covers offers free shipping on all domestic orders placed on our website.</p>
    <p style="margin-top:10.5px">Just because shipping is free doesn't mean it should take a long time. We understand that getting your items quickly is important to you, so we make every effort to process your order quickly. When you order from our website, you can expect to receive your order within 4-5 business days.</p>
    <p style="margin-top:10.5px">If an error is found in the shipping address, please contact us at 1-800-555-0184 as soon as possible and our Support Staff will do their best to update your order with the correct shipping information or intercept the package and correct the destination if it has already shipped.</p>
    <h3 class="h3" style="margin-top:10.5px">Shipping Internationally</h3>
    <p>We will gladly ship your product to Canada; however, these orders are not eligible for free shipping and may be subject to customs fees, taxes, or duties. These fees are not determined until the product crosses the border; therefore, these costs are the responsibility of the customer. Our shipping and handling cost does not include any of these fees.</p>
  </section>

  <!-- sidebar -->
  <aside class="abs side">
    <div class="in price">$286.00</div>
    <div class="in kv" style="top:32px"><b>Regular Price:</b><b>$422.50</b><b>You Save:</b><b>$136.50</b></div>
    <div class="in kv" style="top:55px"><span>Availability:</span><span>Ready to Ship</span><span>Ships:</span><span>1 Business Day</span></div>
    <div class="in kv" style="top:79px;align-items:center"><span>*Color</span><div class="select">Gray</div></div>
    <div class="in kv" style="top:95px;align-items:center"><span>Quantity:</span><div class="select">1</div></div>
    <div class="in free" style="top:110px">Free Shipping*</div>
    <div class="in btn" style="top:127px;width:64px;height:16px">Add to cart</div>
    <div class="in side-h" style="top:156px">Frequently Purchased Together</div>
    <div class="in" style="top:171px">
      <div class="fbt"><div class="pic" role="img" aria-label="Support pole"></div><p><strong>Support Pole</strong><br>Works for Boats and Trucks<br><em>$30.75</em> ☐</p></div>
      <div class="fbt"><div class="pic" role="img" aria-label="Support pole"></div><p><strong>Support Pole</strong><br>Works for Boats and Trucks<br><em>$30.75</em> ☐</p></div>
      <div class="fbt"><div class="pic" role="img" aria-label="Support pole"></div><p><strong>Support Pole</strong><br>Works for Boats and Trucks<br><em>$30.75</em> ☐</p></div>
      <div class="fbt"><div class="pic" role="img" aria-label="Support pole"></div><p><strong>Support Pole</strong><br>Works for Boats and Trucks<br><em>$30.75</em> ☐</p></div>
    </div>
    <div class="in side-h" style="top:339px">Looking for an indoor cover?</div>
    <div class="in box" style="top:356px;height:44px;background:linear-gradient(#fff 20%,#2a3f8f 45%,#c8cfdc 70%,#fff)" role="img" aria-label="Blue cover on a center console boat"></div>
    <div class="in" style="top:403px;font-size:5.8px;line-height:7.5px;color:#333">Support PCenter Console with Bow Railsole</div>
    <p class="in lorem" style="top:427px">Etiam dui justo, vulputate ut mollis eget, volutpat non turpis. Aenean viverra nunc nisi, a eleifend lectus aliquet in. Maecenas laoreet lectus sed est egestas.</p>
    <div class="in ebook-h" style="top:470px">For <span>Free</span> eBook</div>
    <div class="in box" style="top:489px;height:44px;background:linear-gradient(90deg,#fff,#e4e6ea 35%,#fff 50%,#e4e6ea 70%,#fff)" role="img" aria-label="Two ebook covers"></div>
    <p class="in lorem" style="top:544px">Etiam dui justo, vulputate ut mollis eget, volutpat non turpis. Aenean viverra nunc nisi, a eleifend lectus aliquet in. Maecenas laoreet lectus sed est egestas.</p>
    <div class="in email" style="top:582px">Enter your email id</div>
    <div class="in btn" style="top:600px;width:64px;height:16px">Submit for free</div>
  </aside>

  <!-- footer -->
  <div class="abs scene" role="img" aria-label="Marina with sailboats in front of mountains"></div>
  <footer class="abs foot">
    <div class="abs signup">
      <span style="margin-left:9px">Sign Up To Win A FREE Boat Cover!</span>
      <span class="inp"></span><span class="sub">Subscribe ›</span>
      <span class="links"><span>Exchanges &amp; Returns</span><span>Contact Us</span></span>
    </div>
    <div class="abs copy">Copyright © 2016 Hullwrap.com. All Rights Reserved.<br>120 Dockside Lane, Harborview, ME 04000<br><u>Privacy Policy</u></div>
  </footer>

</div>
</div>
</body>
</html>
```